Mezzanine Floor Manufacturer looking for a new business card design

We manufacture mezzanine floors and are providers of racking systems. We provide a range of items/services - simple rack repairs , full warehouse fit outs , manufacturer and install mezzanine floors , partitioning and large turnkey projects. Recently had a new website - www.corvane-shelving.co.uk and would like our business cards updating aswell . Our current card is single sided in the old logo colours (pdf attached) and needs updating.

Target Market(s)

We deal with large projects/ multi national companies and also smaller projects and companies throughout the UK ranging from a single warehouse to a large multi site company.

Industry/Entity Type

Business

Contact Information for Business Card

Will have job title,tel no's, email ,website address etc like example pdf

Requirements
Must have
• Hi - needs to use the colours of the logo & new website. Card needs to be professional

```html
<!DOCTYPE html>
<html lang="en">
<head>
<meta charset="utf-8">
<title>Corvane – Business Card</title>
<link href="https://fonts.googleapis.com/css2?family=Arimo:wght@400;700&display=swap" rel="stylesheet">
<style>
  :root {
    --brand-red: #b71f24;
    --card-white: #f1f1f1;
    --ink: #1c1c1c;
    --backdrop: #232323;
    --faint-red: rgba(183, 31, 36, 0.12);
  }
  * { margin: 0; padding: 0; box-sizing: border-box; }
  html, body { width: 1200px; height: 800px; overflow: hidden; }
  body {
    background: var(--backdrop);
    font-family: "Arimo", Arial, sans-serif;
    position: relative;
  }
  .card {
    position: absolute;
    top: 238px;
    width: 536px;
    height: 306px;
    background: var(--card-white);
    overflow: hidden;
  }
  .card--front { left: 49px; }
  .card--back { left: 617px; }

  /* front */
  .side-band {
    position: absolute; left: 0; top: 0;
    width: 84px; height: 100%;
    background: var(--brand-red);
  }
  .brand-mark {
    position: absolute; left: 44px; top: 58px;
    display: flex; align-items: center; gap: 16px;
  }
  .brand-mark__dot {
    width: 30px; height: 30px; border-radius: 50%;
    background: var(--card-white);
  }
  .brand-mark__name {
    font-size: 40px; font-weight: 700; color: var(--brand-red);
    line-height: 1;
  }
  .backdrop-word {
    position: absolute;
    font-weight: 700; color: var(--faint-red);
    line-height: 1; white-space: nowrap;
  }
  .card--front .backdrop-word { left: 250px; top: 185px; font-size: 96px; }
  .holder {
    position: absolute; right: 30px; top: 112px; text-align: right;
  }
  .holder__name { font-size: 23px; color: var(--brand-red); line-height: 1.1; }
  .holder__role { font-size: 15.5px; color: var(--ink); margin-top: 6px; }
  .divider {
    position: absolute; left: 84px; right: 0; top: 171px;
    height: 2px; background: var(--brand-red); opacity: .85;
  }
  .contacts {
    position: absolute; left: 103px; top: 192px; list-style: none;
  }
  .contacts li {
    display: flex; align-items: center; gap: 10px;
    font-size: 14.5px; color: var(--ink); height: 19.2px;
  }
  .contacts svg { width: 12px; height: 12px; flex: none; }

  /* back */
  .card--back .backdrop-word { left: 60px; top: 52px; font-size: 140px; }
  .company-name {
    position: absolute; left: 0; right: 0; top: 36px;
    text-align: center; font-size: 50px; font-weight: 700;
    color: var(--brand-red); line-height: 1; padding-left: 26px;
  }
  .services-title {
    position: absolute; left: 48px; top: 108px;
    font-size: 20px; color: var(--ink);
  }
  .services {
    position: absolute; top: 150px; list-style: none;
  }
  .services--left { left: 50px; }
  .services--right { left: 313px; top: 148px; }
  .services li {
    display: flex; align-items: center; gap: 12px;
    font-size: 17px; color: var(--ink); height: 24.5px;
  }
  .services li::before {
    content: "✸"; color: var(--brand-red); font-size: 12px; width: 12px;
  }
  .address-band {
    position: absolute; left: 0; right: 0; bottom: 0; height: 38px;
    background: var(--brand-red); color: #fff;
    font-size: 14.5px; display: flex; align-items: center; padding-left: 17px;
    white-space: nowrap;
  }
</style>
</head>
<body>

<section class="card card--front">
  <div class="side-band"></div>
  <div class="backdrop-word" aria-hidden="true">Corvane</div>
  <div class="brand-mark">
    <span class="brand-mark__dot"></span>
    <span class="brand-mark__name">Corvane</span>
  </div>
  <div class="holder">
    <div class="holder__name">Daniel Hartley</div>
    <div class="holder__role">Technical Sales</div>
  </div>
  <div class="divider"></div>
  <ul class="contacts">
    <li><svg viewBox="0 0 12 12"><rect width="12" height="12" fill="#b71f24"/><rect x="4" y="2" width="4" height="8" rx="1" fill="none" stroke="#fff"/></svg>07700900418</li>
    <li><svg viewBox="0 0 12 12"><rect width="12" height="12" fill="#b71f24"/><path d="M3 2.5 L5 2.5 L5.5 4.5 L4.5 5.5 Q5.5 7 6.5 7.5 L7.5 6.5 L9.5 7 L9.5 9 Q5 9.5 3 5 Z" fill="#fff"/></svg>01632 960512</li>
    <li><svg viewBox="0 0 12 12"><rect width="12" height="12" fill="#b71f24"/><rect x="2.5" y="5" width="7" height="3.5" fill="#fff"/><rect x="4" y="2.5" width="4" height="2" fill="#fff"/><rect x="4" y="9" width="4" height="1.5" fill="#fff"/></svg>01632 960734</li>
    <li><svg viewBox="0 0 12 12"><rect width="12" height="12" fill="#b71f24"/><rect x="2.5" y="3.5" width="7" height="5" fill="none" stroke="#fff"/><path d="M2.5 3.5 L6 6.5 L9.5 3.5" fill="none" stroke="#fff"/></svg>daniel@corvane-shelving.co.uk</li>
    <li><svg viewBox="0 0 12 12"><rect width="12" height="12" fill="#b71f24"/><circle cx="6" cy="6" r="3.5" fill="none" stroke="#fff"/><path d="M2.5 6 H9.5 M6 2.5 V9.5" stroke="#fff" stroke-width=".8"/></svg>www.corvane-shelving.co.uk</li>
  </ul>
</section>

<section class="card card--back">
  <div class="backdrop-word" aria-hidden="true">Corvane</div>
  <h1 class="company-name">Corvane</h1>
  <h2 class="services-title" style="font-weight:400">services-</h2>
  <ul class="services services--left">
    <li>Mezzanine Floors</li>
    <li>Cantilever Racking</li>
    <li>Longspan shelving</li>
    <li>Steel Shelving</li>
  </ul>
  <ul class="services services--right">
    <li>Pallet Racking</li>
    <li>Safety Barriers</li>
    <li>Partitioning</li>
    <li>Turnkey Projects</li>
  </ul>
  <div class="address-band">Twelve Mill Lane Ashcombe Trade Park&nbsp; Belford,Derbyshire DE9 4QT</div>
</section>

</body>
</html>
```